Morvell Electric Business Card

An electrical contractor needs a business card design, that will stand out.
I would like designs that use the colors in the logo shown. The logo attached I am ok with but if you have a better idea I am open for suggestions. I like the color scheme.
Industry/Entity Type
Electrical
Contact Information for Business Card
Services, social media, QR code,

```html
<!DOCTYPE html>
<html lang="en">
<head>
<meta charset="utf-8">
<title>Morvell Electric Business Card</title>
<link href="https://fonts.googleapis.com/css2?family=Montserrat:wght@700;800&family=Open+Sans:wght@400;600&display=swap" rel="stylesheet">
<style>
  :root {
    --backdrop: #3b3b3b;
    --card-white: #f7f7f5;
    --card-black: #141414;
    --ink: #1c1a1b;
    --ink-soft: #555555;
    --accent: #e9ac1c;
    --rule: #4a4a4a;
    --emboss: #2a2a2a;
    --emboss-light: #6a6a6a;
  }
  * { box-sizing: border-box; margin: 0; padding: 0; }
  html, body { width: 1200px; height: 801px; overflow: hidden; }
  body {
    background: var(--backdrop);
    font-family: "Open Sans", sans-serif;
    position: relative;
  }
  .card {
    position: absolute;
    top: 252px;
    width: 520px;
    height: 297px;
    box-shadow: 0 12px 30px rgba(0,0,0,0.45);
  }
  .card-front { left: 60px; background: var(--card-white); }
  .card-back { left: 620px; background: var(--card-black); }

  .brand {
    position: absolute;
    left: 34px;
    top: 96px;
    width: 220px;
    text-align: center;
  }
  .brand-square {
    display: block;
    width: 58px;
    height: 58px;
    margin: 0 auto 16px;
    border-radius: 12px;
    background: var(--accent);
  }
  .brand-name {
    font-family: "Montserrat", sans-serif;
    font-weight: 800;
    font-size: 21px;
    letter-spacing: 0.5px;
    color: var(--ink);
    white-space: nowrap;
  }
  .divider {
    position: absolute;
    left: 272px;
    top: 78px;
    width: 1px;
    height: 142px;
    background: var(--rule);
  }
  .contact {
    position: absolute;
    left: 292px;
    top: 76px;
    color: var(--ink-soft);
    font-size: 12.5px;
    line-height: 1.5;
  }
  .contact-name {
    font-family: "Montserrat", sans-serif;
    font-weight: 800;
    font-size: 17px;
    color: var(--ink);
    letter-spacing: 0.3px;
  }
  .contact-title {
    color: var(--accent);
    font-weight: 600;
    font-size: 13px;
    margin-bottom: 4px;
  }
  .contact-address { margin-bottom: 4px; }
  .contact-line { display: flex; align-items: center; gap: 7px; }
  .contact-line svg { width: 11px; height: 11px; flex: none; }

  .back-brand {
    position: absolute;
    inset: 0;
    display: flex;
    flex-direction: column;
    align-items: center;
    justify-content: center;
    gap: 18px;
  }
  .back-square {
    width: 84px;
    height: 84px;
    border-radius: 18px;
    background: var(--emboss);
  }
  .back-name {
    font-family: "Montserrat", sans-serif;
    font-weight: 800;
    font-size: 30px;
    letter-spacing: 0.5px;
    color: var(--emboss-light);
    white-space: nowrap;
  }
</style>
</head>
<body>
  <section class="card card-front">
    <div class="brand">
      <span class="brand-square"></span>
      <p class="brand-name">MORVELL ELECTRIC</p>
    </div>
    <div class="divider"></div>
    <div class="contact">
      <p class="contact-name">DALE HARROW</p>
      <p class="contact-title">President</p>
      <p class="contact-address">3180 Cove Ridge Road<br>Harbor Bend CA 90412</p>
      <p class="contact-line">
        <svg viewBox="0 0 12 12"><circle cx="6" cy="6" r="6" fill="#e9ac1c"/><path d="M4 3.2l1 1.6-.6.6a4 4 0 0 0 2.2 2.2l.6-.6 1.6 1-.6 1C5.5 9 3 6.5 3 3.8z" fill="#fff"/></svg>
        555-014-2290
      </p>
      <p class="contact-line">
        <svg viewBox="0 0 12 12"><rect x="0.5" y="2" width="11" height="8" rx="1" fill="#e9ac1c"/><path d="M1 3l5 3.5L11 3" stroke="#fff" fill="none" stroke-width="1"/></svg>
        dharrow@MorvellElectric.com
      </p>
      <p class="contact-line">
        <svg viewBox="0 0 12 12"><circle cx="6" cy="6" r="5.5" fill="#e9ac1c"/><path d="M0.5 6h11M6 0.5c-2.5 3-2.5 8 0 11M6 0.5c2.5 3 2.5 8 0 11" stroke="#fff" fill="none" stroke-width="0.8"/></svg>
        www.MorvellElectric.com
      </p>
    </div>
  </section>

  <section class="card card-back">
    <div class="back-brand">
      <span class="back-square"></span>
      <p class="back-name">MORVELL ELECTRIC</p>
    </div>
  </section>
</body>
</html>
```